Personal Finance Author needs a postcard

Hi there,

I am a Canadian personal finance author and have published a new book called The Wealth Compass.

I teach Millennials how to create a 6-figure portfolio through investing (https://www.dariafelt.com/)

I'm speaking at some conferences so we were going to print some postcards to hand out to attendees with our info and calls-to-action on them.

I am looking for 4x6 (horizontal) postcard (no space needed for shipping label).

Logos, Headshots and Book Cover:
https://files.cloudvaultex.com/folders/8kQpZrT2mWvN4xLbJ7sHdYc3FgA9eUoRi?usp=sharing

Both sides will be full colour. I would like a clean and simple look. Our main sites are www.DariaFelt.com and www.TheWealthCompassBook.com if you want to get a sense of style and design.
I also uploaded a few marketing materials so you can see the existing designs.

Side 1:
Get Instant Access to your Free Resources - main headline

(small bullets underneath)
- The Wealth Compass Checklist
- Financial Worksheets
- Database of Investment Tools

DariaFelt.com/Resources

At the bottom, include "Don't forget to follow Daria Felt on social media:
Linkedin: @dariafelt7
Facebook: @thewealthcompassbook Instagram: @thewealthcompassbook Twitter: @WealthCompassBk"

Side 2:
Headline - Want to work directly with Daria and The Wealth Compass team to help you make your money grow and stay safe?

Work with us to (bullet point list)...
- Hire Daria as a Keynote Speaker
- Teach Financial Literacy Workshops
- Receive Financial Coaching

Want To Learn More About How We Can Help?
DariaFelt.com/Services

Include my contact info:
Daria Felt
Author | Speaker | Investor
daria@thewealthcompassbook.com
416-555-0187

Target Market(s)

Millennials who want to learn how to save and invest their money. I focus on stock market investing, real estate investing and entrepreneurship.

Industry/Entity Type

Financial Service

Font styles to use
Sans Serif

Colors

Designer to choose colors to be used in the design.

Requirements
Must have
• Photo of Daria Felt
• The Wealth Compass logo
• Green, Gold/Yellow to match existing colours
• modern business style postcard

```html
<!DOCTYPE html>
<html lang="en">
<head>
<meta charset="UTF-8">
<title>The Wealth Compass – Postcard</title>
<link rel="stylesheet" href="https://fonts.googleapis.com/css2?family=Oswald:wght@600&family=Montserrat:wght@400;600;700&family=Raleway:wght@400&family=Libre+Baskerville:wght@700&display=swap">
<style>
  :root {
    --green: #0f6a33;
    --green-deep: #0b5a2b;
    --gold: #ecb83f;
    --gold-light: #f3cc5a;
    --white: #ffffff;
    --ink: #111111;
    --mist: #d2d6c4;
    --sky: #cfe3ea;
    --grey-panel: #e2e2e2;
    --photo-a: #e9e9e9;
    --photo-b: #bdbdbd;
  }
  * { box-sizing: border-box; margin: 0; padding: 0; }
  html, body {
    width: 1200px; height: 393px; overflow: hidden; background: #ffffff;
  }
  .canvas { position: relative; width: 1200px; height: 393px; }

  /* ---------- Side 1 ---------- */
  .side-front {
    position: absolute; left: 101px; top: 23px; width: 450px; height: 331px;
    background: var(--gold); overflow: hidden;
  }
  .front-panel {
    position: absolute; left: 0; top: 0; width: 242px; height: 331px;
    background: var(--green); border-top-right-radius: 16px;
  }
  .brand-block {
    position: absolute; left: 14px; top: 0; width: 196px; height: 140px;
    background: linear-gradient(to bottom, var(--gold) 0%, var(--gold) 45%, var(--green) 100%);
    display: flex; align-items: center; justify-content: center; text-align: center;
  }
  .brand-name {
    font-family: "Oswald", sans-serif; font-weight: 600; color: var(--green-deep);
    font-size: 30px; line-height: 1.05; text-transform: uppercase; letter-spacing: 0.5px;
  }
  .access-band {
    position: absolute; left: 210px; top: 123px; width: 240px; height: 128px;
    background: linear-gradient(to right, var(--green) 0%, var(--green) 15%, var(--gold) 100%);
  }
  .access-headline {
    position: absolute; left: 233px; top: 143px; width: 210px;
    font-family: "Oswald", sans-serif; font-weight: 600; color: var(--white);
    font-size: 21px; line-height: 27px; text-align: center;
  }
  .access-url {
    position: absolute; left: 205px; top: 205px; width: 245px; text-align: center;
    font-family: "Montserrat", sans-serif; font-size: 16px; color: var(--sky);
  }
  .resource-list {
    position: absolute; left: 25px; top: 164px; list-style: none;
    font-family: "Montserrat", sans-serif; font-size: 11px; line-height: 14px; color: var(--mist);
  }
  .resource-list li::before { content: "• "; }
  .follow-note {
    position: absolute; left: 18px; top: 248px; width: 192px; text-align: right;
    font-family: "Raleway", sans-serif; font-size: 18px; line-height: 22px; color: var(--mist);
    white-space: nowrap;
  }
  .social-list {
    position: absolute; left: 246px; top: 262px; list-style: none;
    font-family: "Montserrat", sans-serif; font-size: 10px; line-height: 12.5px; color: var(--white);
  }

  /* ---------- Side 2 ---------- */
  .side-back {
    position: absolute; left: 680px; top: 23px; width: 495px; height: 329px;
    background: var(--green); overflow: hidden;
  }
  .offer-box {
    position: absolute; left: 0; top: 27px; width: 303px; height: 204px;
    background: var(--gold);
  }
  .offer-frame {
    position: absolute; inset: 8px; border: 2px solid var(--white);
  }
  .offer-headline {
    position: absolute; left: 14px; top: 20px; width: 275px; text-align: center;
    font-family: "Montserrat", sans-serif; font-weight: 700; font-size: 12.5px; line-height: 16px;
    color: var(--white);
  }
  .offer-intro {
    position: absolute; left: 0; top: 97px; width: 303px; text-align: center;
    font-family: "Montserrat", sans-serif; font-size: 11px; color: var(--ink);
  }
  .offer-list {
    position: absolute; left: 45px; top: 111px; list-style: none;
    font-family: "Montserrat", sans-serif; font-size: 11px; line-height: 13px; color: var(--ink);
  }
  .offer-list li::before { content: "• "; }
  .portrait { position: absolute; left: 303px; top: 0; width: 192px; height: 231px; }
  .learn-panel {
    position: absolute; left: 49px; top: 231px; width: 191px; height: 79px;
    background: var(--grey-panel);
  }
  .learn-box {
    position: absolute; left: 21px; top: 11px; width: 149px; height: 57px;
    background: var(--white); border: 1.5px solid var(--ink);
    display: flex; align-items: center; justify-content: center; text-align: center;
    font-family: "Montserrat", sans-serif; font-size: 10px; line-height: 12px; color: var(--ink);
  }
  .contact {
    position: absolute; left: 326px; top: 238px;
    font-family: "Libre Baskerville", serif; font-weight: 700; font-size: 8.5px; line-height: 11px;
    color: var(--white);
  }
</style>
</head>
<body>
<div class="canvas">

  <section class="side-front">
    <div class="front-panel"></div>
    <div class="brand-block"><span class="brand-name">The Wealth<br>Compass</span></div>
    <div class="access-band"></div>
    <h1 class="access-headline">Get Instant Access to your Free Resources</h1>
    <p class="access-url">DariaFelt.com/Resources</p>
    <ul class="resource-list">
      <li>The Wealth Compass Checklist</li>
      <li>Financial Worksheets</li>
      <li>Database of Investment Tools</li>
    </ul>
    <p class="follow-note">Don't forget to<br>follow Daria Felt<br>on social media:</p>
    <ul class="social-list">
      <li>Linkedin: @dariafelt7</li>
      <li>Facebook: @thewealthcompassbook</li>
      <li>Instagram: @thewealthcompassbook</li>
      <li>Twitter: @WealthCompassBk</li>
    </ul>
  </section>

  <section class="side-back">
    <div class="offer-box">
      <div class="offer-frame"></div>
      <h2 class="offer-headline">Want to work directly with Daria and The Wealth Compass team to help you make your money grow and stay safe ?</h2>
      <p class="offer-intro">Work with us to</p>
      <ul class="offer-list">
        <li>Hire Daria as a Keynote Speaker</li>
        <li>Teach Financial Literacy Workshops</li>
        <li>Receive Financial Coaching</li>
      </ul>
    </div>

    <svg class="portrait" viewBox="0 0 192 231" role="img" aria-label="Portrait photo of Daria Felt seated on a black bench">
      <defs>
        <linearGradient id="portraitTone" x1="0" y1="0" x2="0" y2="1">
          <stop offset="0" stop-color="var(--photo-a)"/>
          <stop offset="1" stop-color="var(--photo-b)"/>
        </linearGradient>
      </defs>
      <path d="M60 2 H132 Q150 2 162 14 L180 32 Q192 44 192 62 V170 Q192 188 180 200 L162 218 Q150 231 132 231 H60 Q42 231 30 218 L12 200 Q0 188 0 170 V62 Q0 44 12 32 L30 14 Q42 2 60 2 Z" fill="url(#portraitTone)"/>
    </svg>

    <div class="learn-panel">
      <div class="learn-box">Want To Learn More About<br>How We Can Help?<br>DariaFelt.com/Services</div>
    </div>

    <div class="contact">
      Daria Felt<br>
      Author | Speaker | Investor<br>
      daria@thewealthcompassbook.com<br>
      416-555-0187
    </div>
  </section>

</div>
</body>
</html>
```